RV Park - Advertising RV Park using Billboard 12 ft wide by 6 ft tall size

We need a sign for a relatively new RV Park called Bramblewood of Carver RV Park at 2745 Danbury Road, Murphy , NC. The sign should include our web address and phone number. bramblewoodcarverrv.example, 555-314-2967. We would like to see designs that include nice color and no tacky cartoons. Final design should communicate a nice and safe RV Park. We would also like to include quick directions - Just Ahead! Left on Kestrel Rd then left on Danbury Rd. (A nice motor home or RV representation may be nice but not mandatory to be included.) Classic but eye catching design. Sign is 12 ft wide by 6 ft tall in size. Will likely be vinyl printed.

```html
<!DOCTYPE html>
<html lang="en">
<head>
<meta charset="utf-8">
<title>Bramblewood of Carver RV Park – Billboard</title>
<link rel="stylesheet" href="https://fonts.googleapis.com/css2?family=Bebas+Neue&family=Poppins:wght@600;700;800&display=swap">
<style>
  :root {
    --maroon-deep: #4f0c0e;
    --maroon: #6a1214;
    --maroon-light: #7d1a1b;
    --gold: #ecc521;
    --white: #ffffff;
    --ink: #000000;
    --charcoal: #232323;
    --page: #ffffff;
  }
  * { margin: 0; padding: 0; box-sizing: border-box; }
  html, body {
    width: 843px; height: 1200px; overflow: hidden;
    background: var(--page);
  }
  .billboard {
    position: absolute;
    left: 21px; top: 400px;
    width: 800px; height: 400px;
    overflow: hidden;
    box-shadow: 0 10px 40px rgba(0,0,0,0.28);
    font-family: "Poppins", sans-serif;
  }
  .billboard__backdrop {
    position: absolute; inset: 0;
    background:
      radial-gradient(ellipse at 30% 40%, var(--maroon-light) 0%, transparent 60%),
      linear-gradient(170deg, var(--maroon) 0%, var(--maroon-deep) 100%);
  }
  .brand-badge {
    position: absolute;
    left: 32px; top: 36px;
    width: 145px; height: 85px;
    background: var(--white);
    border: 3px solid var(--ink);
    border-radius: 26px;
    display: flex; align-items: center; justify-content: center;
    text-align: center;
  }
  .brand-badge__name {
    font-family: "Poppins", sans-serif;
    font-weight: 600;
    font-size: 15px;
    line-height: 1.15;
    letter-spacing: 1px;
    color: var(--ink);
    text-transform: uppercase;
  }
  .headline {
    position: absolute;
    left: 192px; top: 42px;
    width: 585px;
    height: 76px;
    display: flex; align-items: center; justify-content: center;
    font-family: "Bebas Neue", sans-serif;
    font-weight: 400;
    font-size: 73px;
    line-height: 1;
    color: var(--white);
    white-space: nowrap;
    letter-spacing: -0.5px;
  }
  .park-label {
    position: absolute;
    left: 26px; top: 126px;
    font-weight: 800;
    font-size: 112px;
    line-height: 1;
    letter-spacing: -2px;
    color: var(--gold);
    white-space: nowrap;
  }
  .directions-tag {
    position: absolute;
    left: 558px; top: 140px;
    width: 215px; height: 86px;
    background: var(--charcoal);
    border-radius: 8px;
    padding: 6px 0 0 30px;
    font-weight: 800;
    font-size: 38px;
    line-height: 0.98;
    color: var(--white);
  }
  .phone-band {
    position: absolute;
    left: 0; top: 239px;
    width: 100%; height: 93px;
    background: var(--white);
    display: flex; align-items: center; justify-content: center;
  }
  .phone-band__number {
    font-weight: 800;
    font-size: 100px;
    line-height: 1;
    letter-spacing: -1px;
    color: var(--ink);
    padding-top: 10px;
    white-space: nowrap;
  }
  .web-address {
    position: absolute;
    left: 0; top: 340px;
    width: 100%;
    text-align: center;
    font-weight: 700;
    font-size: 30px;
    letter-spacing: 5px;
    color: var(--white);
    white-space: nowrap;
  }
</style>
</head>
<body>
  <section class="billboard">
    <div class="billboard__backdrop" role="img" aria-label="Dark maroon textured backdrop with faint mountain ridges"></div>

    <div class="brand-badge">
      <span class="brand-badge__name">Bramblewood<br>of Carver</span>
    </div>

    <h1 class="headline">BRAMBLEWOOD OF CARVER</h1>
    <p class="park-label">RV PARK</p>
    <p class="directions-tag">JUST<br>AHEAD!</p>

    <div class="phone-band">
      <p class="phone-band__number">555-314-2967</p>
    </div>

    <p class="web-address">bramblewoodcarverrv.example</p>
  </section>
</body>
</html>
```